PELDIVUX HOA Portal Site for Public

Clean up and organize current website; need website to look good and functional; this is a HOA (homeowner association management) website where homeowners can login and pay their bill, general information about a HOA, monthly newsletter page.
Competitors:
https://lumaridge.example/
https://bexolirnada.example/
https://www.qvhabitations.example/nevada
http://www.tpq-hoa.example/

Target Market(s)

homeowners

Industry/Entity Type

Real Estate

Coding

Coded - Design and coding required

Number of Pages Required

5+ page

Font styles to use
Serif

Colors
0292cd
33a6d7
e667a6
e34297

Requirements
Must have
• login to pay
• services page
• contact us
• order resale package
Nice to have
• page why an HOA would contract us

```html
<!DOCTYPE html>
<html lang="en">
<head>
<meta charset="utf-8">
<title>Peldivux Association Management</title>
<link rel="stylesheet" href="https://fonts.googleapis.com/css2?family=Oswald:wght@300;400;500&family=Poppins:wght@400;500;600&display=swap">
<style>
:root{
  --green:#5ea82f;
  --lime:#8cc63f;
  --blue:#1a7fc8;
  --ink:#222;
  --text:#555;
  --dark:#1f1f1f;
  --mist:#d6ddeb;
  --white:#fff;
}
*{box-sizing:border-box;margin:0;padding:0}
html,body{width:1200px;height:4831px;overflow:hidden}
body{position:relative;background:var(--white);font-family:'Poppins',sans-serif;color:var(--text)}
.abs{position:absolute}
.heading{font-family:'Oswald',sans-serif;font-weight:400;color:var(--ink);text-align:center;font-size:40px;width:1200px;left:0}
.rule{position:absolute;left:571px;width:58px;height:4px;background:var(--green)}
.btn{position:absolute;font-family:'Poppins',sans-serif;font-weight:600;font-size:14px;color:#fff;display:flex;align-items:center;justify-content:center;border-radius:3px;text-transform:uppercase}

/* header */
.site-header{top:0;left:0;width:1200px;height:103px;background:#fff}
.brand{left:140px;top:26px;display:flex;align-items:center;gap:14px}
.brand-mark{width:44px;height:44px;border-radius:50%;background:var(--green)}
.brand-name{font-family:'Oswald',sans-serif;font-weight:500;font-size:30px;letter-spacing:3px;color:var(--ink);line-height:1}
.nav{left:494px;top:38px;display:flex;gap:24px;font-family:'Oswald',sans-serif;font-size:19px;color:#333}
.nav .active{color:var(--green)}
.btn-login{left:911px;top:34px;width:145px;height:40px;background:var(--green);font-size:14px}

/* hero */
.hero{top:103px;left:0;width:1200px;height:665px;background:linear-gradient(135deg,#d9c7ad,#b89470 55%,#8e6d4f);clip-path:polygon(0 0,1200px 0,1200px 581px,600px 665px,0 581px)}
.hero-title{top:430px;left:0;width:1200px;text-align:center;font-family:'Oswald',sans-serif;font-size:66px;line-height:72px;color:#fff;font-weight:400}
.btn-hero{left:503px;top:600px;width:194px;height:44px;background:var(--green)}
.dots{top:680px;left:560px;display:flex;gap:10px}
.dots span{width:14px;height:14px;border-radius:50%;background:#fff;opacity:.9}
.dots span:first-child{border:3px solid #fff;background:transparent;width:18px;height:18px;margin-top:-2px}

/* cards */
.card{top:954px;width:288px;height:392px;background:#fff;box-shadow:0 2px 4px rgba(0,0,0,.15)}
.card-photo{height:180px;border-bottom:4px solid var(--green)}
.card h3{font-family:'Oswald',sans-serif;font-weight:400;font-size:20px;color:var(--ink);text-align:center;margin-top:42px}
.card p{font-size:13px;line-height:25px;text-align:center;padding:8px 22px 0}

/* welcome */
.welcome-photo{top:1431px;left:0;width:700px;height:497px;background:linear-gradient(160deg,#a9c3d8,#a86b50 45%,#5f8a3d 85%)}
.welcome-panel{top:1431px;left:570px;width:630px;height:497px;background:var(--blue);clip-path:polygon(62px 0,630px 0,630px 497px,0 497px)}
.welcome-panel h2{position:absolute;left:100px;top:60px;font-family:'Oswald',sans-serif;font-weight:400;font-size:40px;line-height:48px;color:#fff}
.welcome-panel .bar{position:absolute;left:100px;top:182px;width:76px;height:4px;background:#fff}
.welcome-panel p{position:absolute;left:100px;top:216px;width:400px;font-size:15px;line-height:29px;color:#fff}
.welcome-panel .btn{left:100px;top:384px;width:136px;height:38px;background:var(--lime);font-size:13px;font-weight:500}

/* services */
.svc{width:270px;text-align:center}
.svc h4{font-weight:500;font-size:17px;color:#333;margin-top:6px;letter-spacing:.3px}
.svc p{font-size:13px;line-height:24px;margin-top:8px}
.svc svg{display:block;margin:0 auto}
.hub{left:440px;top:2150px;width:320px;height:320px;border-radius:50%;border:14px solid var(--green);display:flex;align-items:center;justify-content:center}
.hub span{font-family:'Oswald',sans-serif;font-size:40px;letter-spacing:3px;color:var(--ink)}

/* offer */
.offer-photo{top:2659px;left:560px;width:640px;height:497px;background:linear-gradient(135deg,#e9e3da,#b8a38a 50%,#4d4238)}
.offer-panel{top:2659px;left:0;width:632px;height:497px;background:var(--lime);clip-path:polygon(0 0,632px 0,570px 497px,0 497px)}
.offer-panel h2{position:absolute;left:142px;top:52px;font-family:'Oswald',sans-serif;font-weight:400;font-size:40px;color:#fff}
.offer-panel ul{position:absolute;left:142px;top:150px;width:430px;list-style:none;font-size:15px;line-height:31px;color:#fff}
.offer-panel .btn{left:142px;top:390px;width:136px;height:38px;background:var(--dark);font-size:13px;font-weight:500}

/* proposal */
.proposal{top:3156px;left:0;width:1200px;height:654px;background:var(--mist)}
.proposal-photo{top:50px;left:75px;width:488px;height:604px;background:linear-gradient(180deg,#c9b8a8,#8fb0d6 55%,#6e8fb8);border-radius:200px 200px 0 0}
.proposal h2{position:absolute;left:619px;top:80px;font-family:'Oswald',sans-serif;font-weight:400;font-size:38px;color:var(--ink)}
.field{position:absolute;left:622px;width:424px}
.field label{display:block;font-size:14px;color:#333;margin-bottom:6px}
.field .input{height:40px;background:#fff;border:1px solid #bfc6d4}
.btn-submit{left:622px;top:526px;width:224px;height:44px;background:var(--dark)}

/* testimonials */
.quote{width:300px;text-align:center}
.avatar{width:86px;height:86px;border-radius:50%;margin:0 auto;background:linear-gradient(160deg,#cfd6de,#4b5563)}
.quote p{font-size:13px;line-height:25px;margin-top:30px}
.quote .who{font-style:italic;color:var(--lime);margin-top:10px;font-size:13px}

/* footer */
.site-footer{top:4378px;left:0;width:1200px;height:453px;background:var(--dark);clip-path:polygon(0 88px,600px 0,1200px 88px,1200px 453px,0 453px)}
.foot-brand{top:130px;left:0;width:1200px;display:flex;justify-content:center;align-items:center;gap:12px}
.foot-brand .mark{width:36px;height:36px;border-radius:50%;border:3px solid #fff}
.foot-brand span{font-family:'Oswald',sans-serif;font-size:34px;letter-spacing:3px;color:#fff}
.foot-row{left:0;width:1200px;display:flex;justify-content:center;font-family:'Oswald',sans-serif;font-weight:300;color:#fff;font-size:15px}
.contact-row{top:200px;gap:48px}
.contact-row div{display:flex;align-items:center;gap:10px}
.links-row{top:248px;gap:8px}
.copy-row{top:294px}
.socials{top:346px;left:484px;display:flex;gap:11px}
.socials span{width:38px;height:38px;border-radius:50%;border:2px solid var(--lime)}
</style>
</head>
<body>

<header class="site-header abs">
  <div class="brand abs"><span class="brand-mark"></span><span class="brand-name">PELDIVUX</span></div>
  <nav class="nav abs"><span class="active">Home</span><span>About</span><span>Services</span><span>Homeowners</span><span>Contact</span></nav>
  <a class="btn btn-login">Login to pay</a>
</header>

<section class="hero abs" role="img" aria-label="Smiling family sitting on a wooden floor holding a cardboard roof over their heads"></section>
<svg class="abs" style="top:680px;left:0" width="1200" height="100"><polyline points="0,4 600,88 1200,4" fill="none" stroke="#5ea82f" stroke-width="4"/></svg>
<h1 class="hero-title abs">Peldivux Association<br>Management</h1>
<a class="btn btn-hero">Get more info</a>
<div class="dots abs"><span></span><span></span><span></span><span></span></div>

<h2 class="heading abs" style="top:822px">What Do We Do</h2>
<div class="rule" style="top:907px"></div>

<article class="card abs" style="left:144px">
  <div class="card-photo" role="img" aria-label="Team of managers meeting around a table" style="background:linear-gradient(135deg,#e6dccf,#9b7f68 50%,#2d4a78)"></div>
  <h3>HOA Management</h3>
  <p>Sed ut perspiciatis unde omnis iste natus voluptatem accusantium doloremque laudantium, totam rem aperiam, eaque ipsa quae</p>
</article>
<article class="card abs" style="left:456px">
  <div class="card-photo" role="img" aria-label="Apartment buildings under a blue sky" style="background:linear-gradient(180deg,#3f86d9,#a3644a 55%,#4b7c3a)"></div>
  <h3>Property Management</h3>
  <p>Sed ut perspiciatis unde omnis iste natus voluptatem accusantium doloremque laudantium, totam rem aperiam, eaque ipsa quae</p>
</article>
<article class="card abs" style="left:767px">
  <div class="card-photo" role="img" aria-label="Small wooden house model on documents beside a laptop" style="background:linear-gradient(135deg,#3a5a8a,#c9a27a 50%,#e8e4dc)"></div>
  <h3>Document Request</h3>
  <p>Sed ut perspiciatis unde omnis iste natus voluptatem accusantium doloremque laudantium, totam rem aperiam, eaque ipsa quae</p>
</article>

<div class="welcome-photo abs" role="img" aria-label="Residential apartment complex with flower beds"></div>
<section class="welcome-panel abs">
  <h2>Welcome to Peldivux<br>Association Management</h2>
  <div class="bar"></div>
  <p>Sed ut perspiciatis unde omnis iste natus error sit vm doloremque laudantium, totam rem aperiam, eaque ipsa quae ab illo inventore veritatis et quasi archicto beatae vitae dicta sunt explicabo. Nemo enim ipsam voluptatem quia voluptas sit aspernatur</p>
  <a class="btn">Read more</a>
</section>

<h2 class="heading abs" style="top:2000px">Our Services</h2>
<div class="rule" style="top:2078px"></div>

<svg class="abs" style="top:0;left:0" width="1200" height="2600">
  <g fill="none" stroke="#333" stroke-width="1.5">
    <polyline points="388,2136 486,2136 486,2231"/>
    <polyline points="785,2136 690,2136 690,2231"/>
    <line x1="388" y1="2391" x2="440" y2="2391"/>
    <line x1="760" y1="2391" x2="785" y2="2391"/>
    <circle cx="382" cy="2136" r="5" fill="#fff"/>
    <circle cx="791" cy="2136" r="5" fill="#fff"/>
    <circle cx="382" cy="2391" r="5" fill="#fff"/>
    <circle cx="791" cy="2391" r="5" fill="#fff"/>
  </g>
</svg>
<div class="hub abs"><span>PELDIVUX</span></div>

<div class="svc abs" style="left:137px;top:2120px">
  <svg width="76" height="66" viewBox="0 0 76 66" fill="none" stroke="#333" stroke-width="2"><path d="M4 62h68M10 62V36h10v26M26 62V26h10v26M42 62V40h10v22"/><path d="M8 26l16-12 12 8 24-18"/><path d="M54 4h8v8"/><circle cx="60" cy="50" r="10"/></svg>
  <h4>Pay Assessments</h4>
  <p>Sed ut perspiciatis unde omnis iste natus error sit voluptatem accusantium doloremque laudantium</p>
</div>
<div class="svc abs" style="left:791px;top:2120px">
  <svg width="76" height="66" viewBox="0 0 76 66" fill="none" stroke="#333" stroke-width="2"><rect x="10" y="2" width="52" height="62" rx="3"/><circle cx="26" cy="18" r="8"/><path d="M40 14h16M40 22h16M18 40l8-6 8 6 8-6 8 6M18 52h36"/><path d="M66 6v54"/></svg>
  <h4>Developers</h4>
  <p>Sed ut perspiciatis unde omnis iste natus error sit voluptatem accusantium doloremque laudantium</p>
</div>
<div class="svc abs" style="left:137px;top:2357px">
  <svg width="76" height="66" viewBox="0 0 76 66" fill="none" stroke="#5ea82f" stroke-width="2"><circle cx="20" cy="40" r="6"/><circle cx="38" cy="40" r="6"/><circle cx="56" cy="40" r="6"/><path d="M10 62c0-8 20-8 20 0M28 62c0-8 20-8 20 0M46 62c0-8 20-8 20 0"/><rect x="30" y="4" width="36" height="24"/><path d="M36 22v-6M44 22v-10M52 22v-14M60 22v-8"/></svg>
  <h4>Leadership Team</h4>
  <p>Sed ut perspiciatis unde omnis iste natus error sit voluptatem accusantium doloremque laudantium</p>
</div>
<div class="svc abs" style="left:791px;top:2357px">
  <svg width="76" height="66" viewBox="0 0 76 66" fill="none" stroke="#5ea82f" stroke-width="2"><circle cx="38" cy="30" r="16"/><circle cx="38" cy="30" r="6"/><path d="M38 4v8M38 48v8M12 30h8M56 30h8M20 12l6 6M56 12l-6 6M8 62h60"/></svg>
  <h4>Association Management</h4>
  <p>Sed ut perspiciatis unde omnis iste natus error sit voluptatem accusantium doloremque laudantium</p>
</div>

<div class="offer-photo abs" role="img" aria-label="Hand signing a document with a fountain pen"></div>
<section class="offer-panel abs">
  <h2>We offer</h2>
  <ul>
    <li>Accessible, licensed Association Managers</li>
    <li>24 hour Web site access: online account information</li>
    <li>24 hour emergency service</li>
    <li>Provide monthly financial reports to the Board of Directors</li>
    <li>Read, study and understand all governing documents of the Association. Correspond with members in violation of the CC&amp;Rs, By-laws, Rules &amp; Regulations</li>
  </ul>
  <a class="btn">Read more</a>
</section>

<section class="proposal abs">
  <div class="proposal-photo abs" role="img" aria-label="Young woman in a denim shirt holding a laptop"></div>
  <h2>Request a Free Proposal Now!</h2>
  <div class="field" style="top:166px"><label>Name *</label><div class="input"></div></div>
  <div class="field" style="top:251px"><label>Phone *</label><div class="input"></div></div>
  <div class="field" style="top:328px"><label>Email *</label><div class="input"></div></div>
  <div class="field" style="top:406px"><label>Message</label><div class="input" style="height:66px"></div></div>
  <a class="btn btn-submit">Submit</a>
</section>

<h2 class="heading abs" style="top:3875px">Client Testimonials</h2>
<div class="rule" style="top:3956px;background:var(--ink)"></div>
<svg class="abs" style="top:4007px;left:413px" width="360" height="290"><polygon points="82,2 278,2 358,144 278,286 82,286 2,144" fill="none" stroke="#8cc63f" stroke-width="2"/></svg>

<div class="quote abs" style="left:113px;top:4031px">
  <div class="avatar" role="img" aria-label="Client portrait"></div>
  <p>Sed ut perspiciatis unde omnis iste natus error sit voluptatem accusantium doloremque laudantium, totam rem aperiam, eaque ipsa quae ab</p>
  <div class="who">Velmora, K.</div>
</div>
<div class="quote abs" style="left:444px;top:4031px">
  <div class="avatar" role="img" aria-label="Client portrait"></div>
  <p>Sed ut perspiciatis unde omnis iste natus error sit voluptatem accusantium doloremque laudantium, totam rem aperiam, eaque ipsa quae ab</p>
  <div class="who">Velmora, K.</div>
</div>
<div class="quote abs" style="left:784px;top:4031px">
  <div class="avatar" role="img" aria-label="Client portrait"></div>
  <p>Sed ut perspiciatis unde omnis iste natus error sit voluptatem accusantium doloremque laudantium, totam rem aperiam, eaque ipsa quae ab</p>
  <div class="who">Velmora, K.</div>
</div>

<svg class="abs" style="top:4370px;left:0" width="1200" height="100"><polyline points="0,96 600,8 1200,96" fill="none" stroke="#5ea82f" stroke-width="4"/></svg>
<footer class="site-footer abs">
  <div class="foot-brand abs"><span class="mark"></span><span>PELDIVUX</span></div>
  <div class="foot-row contact-row abs">
    <div><svg width="12" height="16" viewBox="0 0 12 16"><path d="M6 0a6 6 0 0 0-6 6c0 4 6 10 6 10s6-6 6-10a6 6 0 0 0-6-6zm0 8a2 2 0 1 1 0-4 2 2 0 0 1 0 4z" fill="#8cc63f"/></svg>2750 W. Quillan Ave, Ste 310 Marlow Springs, Nevada</div>
    <div><svg width="14" height="14" viewBox="0 0 14 14"><path d="M3 0l3 3-2 2c1 2 3 4 5 5l2-2 3 3-2 3C6 14 0 8 0 2z" fill="#8cc63f"/></svg>Call +1 555-014-2287</div>
    <div><svg width="16" height="12" viewBox="0 0 16 12"><rect width="16" height="12" fill="#8cc63f"/><path d="M0 0l8 6 8-6" fill="none" stroke="#1f1f1f" stroke-width="1.5"/></svg>info@peldivux.example</div>
  </div>
  <div class="foot-row links-row abs">Home | Association Management | Services | Homeowners | About Us | Leadership Team | Contact Us</div>
  <div class="foot-row copy-row abs">© 2019 Peldivux Association Management, LLC. All Rights Reserved | Privacy Policy | Terms and Conditions</div>
  <div class="socials abs"><span></span><span></span><span></span><span></span><span></span></div>
</footer>

</body>
</html>
```